Phone Repair Business Card

I need a business card for my mobile phone/ smart phone and tablet repair business based in New Zealand. My business name is "T.K. Repairs". I would like to see a designer make a modern phone related business card, which could incorporate something to do with the Zorvel Kavlo as this is our main repaired product. i like the dark Grey and lime green colours

```html
<!DOCTYPE html>
<html lang="en">
<head>
<meta charset="utf-8">
<title>T.K. Repairs — Business Card</title>
<link rel="stylesheet" href="https://fonts.googleapis.com/css2?family=Kalam:wght@700&family=Tinos&family=Arimo&display=swap">
<style>
  :root {
    --page-bg: #e9eaec;
    --lime: #52ec00;
    --lime-deep: #3fc400;
    --charcoal: #3a3c40;
    --charcoal-deep: #2e3033;
    --silver: #c9cacc;
    --white: #ffffff;
    --ink: #0b0b0b;
    --pin-red: #e8231b;
    --screen-green: #1f4a10;
  }
  * { margin: 0; padding: 0; box-sizing: border-box; }
  html, body {
    width: 1200px; height: 720px; overflow: hidden;
    background: var(--page-bg);
  }
  .card {
    position: absolute; left: 40px; top: 44px;
    width: 1120px; height: 631px;
    overflow: hidden;
    box-shadow: 0 10px 30px rgba(0,0,0,0.25);
  }
  .card__top {
    position: absolute; left: 0; top: 0; width: 100%; height: 431px;
    background: radial-gradient(ellipse at 50% 40%, var(--lime) 0%, var(--lime) 60%, var(--lime-deep) 100%);
  }
  .card__divider {
    position: absolute; left: 0; top: 431px; width: 100%; height: 10px;
    background: linear-gradient(to bottom, #e4e5e6, var(--silver) 50%, #9a9b9d);
  }
  .card__bottom {
    position: absolute; left: 0; top: 441px; width: 100%; height: 190px;
    background: linear-gradient(to bottom, var(--charcoal), var(--charcoal-deep));
  }
  .brand-mark {
    position: absolute; left: 26px; top: 92px;
    display: flex; align-items: center; gap: 10px;
  }
  .brand-mark__dot {
    width: 18px; height: 18px; border-radius: 50%;
    background: var(--white);
  }
  .brand-mark__name {
    font-family: "Tinos", serif; font-size: 34px;
    color: var(--white);
  }
  .business-name {
    position: absolute; left: 0; top: 118px; width: 1120px;
    text-align: center;
    font-family: "Kalam", cursive; font-weight: 700; font-size: 104px;
    color: var(--white);
    text-shadow: 3px 4px 6px rgba(0,0,0,0.75);
    letter-spacing: 1px;
  }
  .device-art {
    position: absolute; left: 1013px; top: 258px;
    width: 74px; height: 155px; border-radius: 10px;
    background: linear-gradient(160deg, #2b5f14 0%, var(--screen-green) 55%, #0d1a08 100%);
    box-shadow: 0 0 0 3px var(--ink), 2px 4px 8px rgba(0,0,0,0.5);
  }
  .contact {
    position: absolute; display: flex; align-items: center;
  }
  .contact--location { left: 6px; top: 535px; }
  .contact--phone { left: 815px; top: 551px; }
  .contact__text--location {
    margin-left: 38px;
    font-family: "Tinos", serif; font-size: 37px; color: var(--white);
  }
  .contact__text--phone {
    margin-left: 26px;
    font-family: "Arimo", sans-serif; font-size: 33px; color: var(--white);
  }
</style>
</head>
<body>
  <main class="card">
    <section class="card__top">
      <div class="brand-mark">
        <span class="brand-mark__dot"></span>
        <span class="brand-mark__name">Zorvel</span>
      </div>
      <h1 class="business-name">T.K. Repairs</h1>
      <div class="device-art" role="img" aria-label="Illustration of a Kavlo smartphone with a green screen"></div>
    </section>
    <div class="card__divider"></div>
    <section class="card__bottom"></section>

    <div class="contact contact--location">
      <svg class="contact__icon" width="36" height="64" viewBox="0 0 36 64" aria-hidden="true">
        <path d="M18 2 C8 2 1 9 1 19 C1 31 18 62 18 62 C18 62 35 31 35 19 C35 9 28 2 18 2 Z" fill="var(--pin-red)"/>
        <circle cx="18" cy="18" r="6" fill="var(--charcoal-deep)"/>
      </svg>
      <span class="contact__text--location">Newzeeland</span>
    </div>

    <div class="contact contact--phone">
      <svg class="contact__icon" width="70" height="70" viewBox="0 0 70 70" aria-hidden="true">
        <circle cx="35" cy="35" r="32" fill="none" stroke="var(--ink)" stroke-width="4"/>
        <path d="M24 18 L31 16 L35 27 L30 31 C32 37 35 41 40 44 L44 39 L55 44 L52 51 C50 54 46 55 42 53 C31 48 23 39 19 28 C18 23 20 20 24 18 Z" fill="var(--ink)"/>
      </svg>
      <span class="contact__text--phone">003 987654</span>
    </div>
  </main>
</body>
</html>
```